Fun label for kids Afro and curly hair brand

A label for a 250 ml Boston bottle. For a moisturiser detangler and leave in conditioner formulated for kids to help with pain free detangling and provide maximum moisture and conditioner. We want children with this hair texture to love their hair.
Target Market(s)
Afro and curly haired children and their parents
Industry/Entity Type
Beauty and cosmetics
Font styles to use
Serif
Colors
Designer to choose colors to be used in the design.
Requirements
Must have
- Logo.Developed for especially children. Label must be wound round the bottle with a right hand leading edge on a 76mm core. Must state the product is free from parabens, sulphates.
Nice to have
- Stand out colours.
Should not have
- N. A

```html
<!DOCTYPE html>
<html lang="en">
<head>
<meta charset="utf-8">
<title>Coily Kin – Moisturiser Detangler &amp; Leave-in Conditioner Label</title>
<link rel="stylesheet" href="https://fonts.googleapis.com/css2?family=Delius&family=Montserrat:ital,wght@0,300;0,400;0,700;1,300&display=swap">
<style>
  :root {
    --backdrop: #1f1f1f;
    --label-black: #0f0f0f;
    --label-edge: #1a1a1a;
    --amber: #e0892b;
    --amber-soft: #c97a2a;
    --copper: #b8732f;
    --magenta: #b24ea8;
    --rose: #d9709c;
    --cocoa: #6b3a22;
    --gold-hair: #efc34a;
    --hair-shadow: #7a2a1e;
  }
  * { margin: 0; padding: 0; box-sizing: border-box; }
  html, body {
    width: 1200px;
    height: 1094px;
    overflow: hidden;
    background: var(--backdrop);
  }
  .canvas {
    width: 1200px;
    height: 1094px;
    display: flex;
    align-items: center;
    justify-content: center;
  }
  .label {
    position: relative;
    width: 470px;
    height: 1000px;
    background: var(--label-black);
    border: 1px solid var(--label-edge);
    display: flex;
    flex-direction: column;
    align-items: center;
    padding: 44px 12px 0;
    overflow: hidden;
  }
  .tagline {
    font-family: "Montserrat", sans-serif;
    font-weight: 700;
    font-size: 14px;
    letter-spacing: 0.16em;
    color: var(--amber);
    white-space: nowrap;
  }
  .brand {
    margin-top: 30px;
    width: 140px;
    height: 140px;
    border: 1.5px solid var(--copper);
    border-radius: 50%;
    display: flex;
    flex-direction: column;
    align-items: center;
    justify-content: center;
    text-align: center;
  }
  .brand-name {
    font-family: "Montserrat", sans-serif;
    font-weight: 400;
    font-size: 20px;
    line-height: 1.2;
    color: #f2f2f2;
  }
  .brand-name small {
    display: block;
    font-size: 7px;
    letter-spacing: 0.3em;
    margin-top: 6px;
  }
  .mascot-art {
    margin-top: 40px;
    width: 400px;
    height: 400px;
    flex-shrink: 0;
    background:
      radial-gradient(circle at 50% 55%, var(--cocoa) 0 22%, rgba(107,58,34,0) 24%),
      radial-gradient(ellipse 34% 40% at 58% 50%, var(--rose) 0 70%, rgba(217,112,156,0) 100%),
      radial-gradient(ellipse 40% 46% at 48% 50%, var(--magenta) 0 60%, rgba(178,78,168,0) 100%),
      radial-gradient(ellipse 46% 48% at 55% 56%, rgba(239,195,74,0.45) 0 55%, rgba(239,195,74,0) 100%),
      radial-gradient(ellipse 50% 50% at 50% 50%, rgba(122,42,30,0.5) 0 50%, rgba(122,42,30,0) 100%);
  }
  .product-name {
    margin-top: 34px;
    font-family: "Delius", cursive;
    font-weight: 400;
    font-size: 31px;
    line-height: 1.3;
    color: var(--amber);
    text-align: center;
  }
  .claims {
    margin-top: 30px;
    display: flex;
    gap: 18px;
  }
  .claim-badge {
    width: 96px;
    height: 96px;
    border: 1.5px solid var(--copper);
    border-radius: 50%;
    display: flex;
    flex-direction: column;
    align-items: center;
    justify-content: center;
    font-family: "Montserrat", sans-serif;
    font-style: italic;
    font-weight: 300;
    font-size: 18px;
    line-height: 1.2;
    color: var(--amber-soft);
  }
  .volume {
    margin-top: 22px;
    font-family: "Montserrat", sans-serif;
    font-weight: 300;
    font-size: 28px;
    color: var(--amber);
  }
</style>
</head>
<body>
<main class="canvas">
  <section class="label">
    <p class="tagline">DEVELOPED FOR ESPECIALLY CHILDREN</p>

    <div class="brand">
      <p class="brand-name">Coily Kin<small>HAIR PRODUCTS</small></p>
    </div>

    <div class="mascot-art" role="img" aria-label="Illustration of a friendly cartoon unicorn with long pink, magenta and gold mane surrounded by purple and orange butterflies"></div>

    <h1 class="product-name">Moisturiser Detangler<br>&amp; Leave-in Conditioner</h1>

    <div class="claims">
      <div class="claim-badge"><span>paraben</span><span>FREE</span></div>
      <div class="claim-badge"><span>sulphate</span><span>FREE</span></div>
    </div>

    <p class="volume">250 ml</p>
  </section>
</main>
</body>
</html>
```